Create a channel art for human resources youtube channel

We a are human resource company that want to develop a community on youtube. Our channel is call "TKV Corner" and we will produce videos related to human resources topics like: Strategy, Job Description, selection of workers, workers development, Occupational health, Training, etc.

We need a channel art for our youtube channel that communicate to our viewers what is about the channel.

Attach you can see the logo and icon of the channel, also you can see it here: https://www.vidzora-example.net/channel/QXpLmWt7bRc3dYhFvKaNsEeZ

Target Market(s)

The people who is going to see the art - banner for youtube are persons that work on human resources field

Industry/Entity Type

Business

Font styles to use
Sans Serif

Requirements
Must have
• Must to communicate that our channel is about how to do a better and faster human resources to help business improve there productivity , also workers performances and quality work life. Here are some key words to help you inspire:
• Human Resources
• Performance
• Better
• Faster
• Easier
• Business
• Improve
• Health

```html
<!DOCTYPE html>
<html lang="en">
<head>
<meta charset="utf-8">
<title>TKV Corner – Channel Art</title>
<link rel="stylesheet" href="https://fonts.googleapis.com/css2?family=Lato:wght@300;400;700;900&display=swap">
<style>
  :root {
    --page: #f2f3f5;
    --banner: #e8ebee;
    --map-tone: #dfe3e8;
    --ink: #2b2d2f;
    --ink-soft: #4a4d50;
    --green: #7ab640;
    --red: #e23b3b;
    --blue: #2fa9e1;
    --yellow: #f2b51c;
    --white: #ffffff;
  }
  * { box-sizing: border-box; margin: 0; padding: 0; }
  html, body { width: 1200px; height: 675px; overflow: hidden; background: var(--page); }
  body { font-family: "Lato", sans-serif; color: var(--ink); }

  .canvas { position: relative; width: 1200px; height: 675px; overflow: hidden; background: var(--page); }

  .banner {
    position: absolute; left: 0; width: 1200px; height: 216px;
    background: var(--banner);
    box-shadow: 0 6px 14px rgba(0,0,0,0.12);
    overflow: hidden;
  }
  .banner--green { top: 80px; }
  .banner--colour { top: 368px; }

  .world-backdrop {
    position: absolute; left: 200px; top: 0; width: 600px; height: 216px;
    background: radial-gradient(ellipse at 45% 55%, var(--map-tone) 0%, rgba(223,227,232,0.4) 45%, rgba(232,235,238,0) 75%);
  }

  .brand-tile {
    position: absolute; left: 34px; top: 8px; width: 98px; height: 96px;
    background: var(--white);
    display: flex; flex-direction: column; align-items: center; justify-content: center; gap: 8px;
    box-shadow: 0 1px 3px rgba(0,0,0,0.08);
  }
  .brand-dot { width: 24px; height: 24px; border-radius: 50%; background: var(--green); }
  .brand-name { font-weight: 700; font-size: 14px; color: var(--ink-soft); text-align: center; line-height: 1.1; }

  .headline { position: absolute; left: 230px; top: 10px; width: 466px; text-align: center; }
  .headline__lead { font-size: 26px; font-weight: 400; color: var(--ink); line-height: 1.15; }
  .headline__main { font-size: 44px; line-height: 1.05; white-space: nowrap; }
  .headline__main .accent { font-weight: 900; color: var(--green); }
  .headline__main .strong { font-weight: 900; color: var(--ink); }
  .banner--colour .headline__main .accent { font-weight: 300; color: var(--ink); }

  .benefits { position: absolute; left: 265px; top: 96px; display: flex; gap: 33px; }
  .benefit { position: relative; width: 75px; height: 85px; }
  .benefit svg { position: absolute; inset: 0; }
  .benefit__label {
    position: absolute; left: 0; right: 0; top: 54px;
    text-align: center; color: var(--white); font-weight: 700; font-size: 11px; letter-spacing: 0.3px;
  }

  .team-photo {
    position: absolute; left: 754px; top: 0; width: 416px; height: 216px;
    background: linear-gradient(90deg, rgba(232,235,238,0) 0%, #cdd3da 12%, #b9c4d2 30%, #f4f5f7 50%, #c9b79f 68%, #a9c1e0 85%, rgba(232,235,238,0) 100%);
    opacity: 0.85;
  }
</style>
</head>
<body>
<div class="canvas">

  <section class="banner banner--green">
    <div class="world-backdrop" role="img" aria-label="Faint world map backdrop"></div>
    <div class="brand-tile"><span class="brand-dot"></span><span class="brand-name">TKV Corner</span></div>
    <div class="headline">
      <p class="headline__lead">Simple Solutions For</p>
      <p class="headline__main"><span class="accent">PEOPLES</span> <span class="strong">PROPLEMS!</span></p>
    </div>
    <div class="benefits">
      <div class="benefit">
        <svg viewBox="0 0 80 90" width="75" height="85"><polygon points="40,4 75,24 75,66 40,86 5,66 5,24" fill="var(--green)" stroke="var(--green)" stroke-width="6" stroke-linejoin="round"/>
          <path d="M30 30h6v18h-6z M38 48V31l6-10c3 0 4 2 3 5l-2 5h8c2 0 3 2 3 3l-3 11c-1 2-2 3-4 3z" fill="var(--white)"/></svg>
        <span class="benefit__label">BETTER</span>
      </div>
      <div class="benefit">
        <svg viewBox="0 0 80 90" width="75" height="85"><polygon points="40,4 75,24 75,66 40,86 5,66 5,24" fill="var(--green)" stroke="var(--green)" stroke-width="6" stroke-linejoin="round"/>
          <path d="M32 22h3v30h-3z M35 23c6-3 10 3 18 0v14c-8 3-12-3-18 0z" fill="var(--white)"/></svg>
        <span class="benefit__label">FASTER</span>
      </div>
      <div class="benefit">
        <svg viewBox="0 0 80 90" width="75" height="85"><polygon points="40,4 75,24 75,66 40,86 5,66 5,24" fill="var(--green)" stroke="var(--green)" stroke-width="6" stroke-linejoin="round"/>
          <path d="M34 20v28l7-6 5 10 4-2-5-10h9z" fill="var(--white)"/></svg>
        <span class="benefit__label">EASIER</span>
      </div>
      <div class="benefit">
        <svg viewBox="0 0 80 90" width="75" height="85"><polygon points="40,4 75,24 75,66 40,86 5,66 5,24" fill="var(--green)" stroke="var(--green)" stroke-width="6" stroke-linejoin="round"/>
          <path d="M28 42h5v9h-5z M35 38h5v13h-5z M42 34h5v17h-5z M49 30h5v21h-5z" fill="var(--white)"/>
          <path d="M27 36l10-8 6 4 11-10" stroke="var(--white)" stroke-width="2.5" fill="none"/><path d="M50 20h7v7z" fill="var(--white)"/></svg>
        <span class="benefit__label">IMPROVE</span>
      </div>
    </div>
    <div class="team-photo" role="img" aria-label="Photo of five smiling business people in shirts and suits, arms crossed"></div>
  </section>

  <section class="banner banner--colour">
    <div class="world-backdrop" role="img" aria-label="Faint world map backdrop"></div>
    <div class="brand-tile"><span class="brand-dot"></span><span class="brand-name">TKV Corner</span></div>
    <div class="headline">
      <p class="headline__lead">Simple Solutions For</p>
      <p class="headline__main"><span class="accent">PEOPLES</span> <span class="strong">PROPLEMS!</span></p>
    </div>
    <div class="benefits">
      <div class="benefit">
        <svg viewBox="0 0 80 90" width="75" height="85"><polygon points="40,4 75,24 75,66 40,86 5,66 5,24" fill="var(--red)" stroke="var(--red)" stroke-width="6" stroke-linejoin="round"/>
          <path d="M30 30h6v18h-6z M38 48V31l6-10c3 0 4 2 3 5l-2 5h8c2 0 3 2 3 3l-3 11c-1 2-2 3-4 3z" fill="var(--white)"/></svg>
        <span class="benefit__label">BETTER</span>
      </div>
      <div class="benefit">
        <svg viewBox="0 0 80 90" width="75" height="85"><polygon points="40,4 75,24 75,66 40,86 5,66 5,24" fill="var(--blue)" stroke="var(--blue)" stroke-width="6" stroke-linejoin="round"/>
          <path d="M32 22h3v30h-3z M35 23c6-3 10 3 18 0v14c-8 3-12-3-18 0z" fill="var(--white)"/></svg>
        <span class="benefit__label">FASTER</span>
      </div>
      <div class="benefit">
        <svg viewBox="0 0 80 90" width="75" height="85"><polygon points="40,4 75,24 75,66 40,86 5,66 5,24" fill="var(--yellow)" stroke="var(--yellow)" stroke-width="6" stroke-linejoin="round"/>
          <path d="M34 20v28l7-6 5 10 4-2-5-10h9z" fill="var(--white)"/></svg>
        <span class="benefit__label">EASIER</span>
      </div>
      <div class="benefit">
        <svg viewBox="0 0 80 90" width="75" height="85"><polygon points="40,4 75,24 75,66 40,86 5,66 5,24" fill="var(--green)" stroke="var(--green)" stroke-width="6" stroke-linejoin="round"/>
          <path d="M28 42h5v9h-5z M35 38h5v13h-5z M42 34h5v17h-5z M49 30h5v21h-5z" fill="var(--white)"/>
          <path d="M27 36l10-8 6 4 11-10" stroke="var(--white)" stroke-width="2.5" fill="none"/><path d="M50 20h7v7z" fill="var(--white)"/></svg>
        <span class="benefit__label">IMPROVE</span>
      </div>
    </div>
    <div class="team-photo" role="img" aria-label="Photo of five smiling business people in shirts and suits, arms crossed"></div>
  </section>

</div>
</body>
</html>
```